BRL Design Business Card

I need to develop a business card for my real estate design and investment company. Something clean, classic and professional with a modern vibe.

Industry/Entity Type

Real Estate

Font styles to use
Serif
Sans Serif

```html
<!DOCTYPE html>
<html lang="en">
<head>
<meta charset="utf-8">
<title>BRL Design Business Card</title>
<link href="https://fonts.googleapis.com/css2?family=Arimo:wght@400;600&display=swap" rel="stylesheet">
<style>
  :root {
    --backdrop: #e4e4e4;
    --card-light: #f7f7f6;
    --card-dark: #1c1c1c;
    --ink: #1a1a1a;
    --ink-soft: #2b2b2b;
    --paper-text: #f2f2f2;
  }
  * { margin: 0; padding: 0; box-sizing: border-box; }
  html, body {
    width: 1200px;
    height: 720px;
    overflow: hidden;
    background: var(--backdrop);
  }
  .stage {
    position: relative;
    width: 1200px;
    height: 720px;
  }
  .card {
    position: absolute;
    top: 242px;
    width: 420px;
    height: 240px;
  }
  .card--front { left: 147px; background: var(--card-light); color: var(--ink); }
  .card--back { left: 633px; background: var(--card-dark); color: var(--paper-text); }

  .brand-name {
    font-family: "Arimo", sans-serif;
    font-weight: 400;
    line-height: 1;
    white-space: nowrap;
  }

  .card--front .brand-name {
    position: absolute;
    left: 40px;
    top: 58px;
    font-size: 25px;
  }

  .person { position: absolute; left: 40px; top: 170px; font-family: "Arimo", sans-serif; }
  .person-name { font-size: 13px; font-weight: 600; line-height: 1.1; }
  .person-role { font-size: 9.5px; margin-top: 2px; }

  .contact {
    position: absolute;
    left: 265px;
    top: 107px;
    width: 140px;
    font-family: "Arimo", sans-serif;
    font-size: 9.5px;
    line-height: 12px;
    color: var(--ink-soft);
  }
  .contact-address { margin-bottom: 16px; }

  .rule {
    position: absolute;
    left: 0;
    top: 211px;
    width: 259px;
    height: 1.5px;
    background: var(--ink);
  }
  .website {
    position: absolute;
    left: 265px;
    top: 206px;
    font-family: "Arimo", sans-serif;
    font-size: 9.5px;
    color: var(--ink-soft);
  }

  .card--back .brand-name {
    position: absolute;
    left: 0;
    right: 0;
    top: 103px;
    text-align: center;
    font-size: 30px;
  }
</style>
</head>
<body>
  <main class="stage">
    <section class="card card--front" aria-label="Business card front">
      <div class="brand-name">BRL Design</div>

      <div class="person">
        <p class="person-name">Daniel Reyes</p>
        <p class="person-role">Founder &amp; CEO</p>
      </div>

      <div class="contact">
        <p class="contact-address">Here your compnay or home address</p>
        <p>+100 555 0142</p>
        <p>+100 555 0187</p>
        <p>info@brl.com</p>
      </div>

      <div class="rule"></div>
      <p class="website">www.brl.com</p>
    </section>

    <section class="card card--back" aria-label="Business card back">
      <div class="brand-name">BRL Design</div>
    </section>
  </main>
</body>
</html>
```